Dental specialist needs a sharp looking letterhead

I am looking for a letterhead to be used to send letters and communication between myself (a dental specialist) and other dentists.
My office is a state of the art dental specialty office.
I need to letterhead to also state:
Gideon R. Whitfield DDS
2847 Birchmont Avenue, Suite K
West Harlow, NY 14391
(716)482-9163
fax: (716)482-9170
whitfieldroot.com (**this email address may change)

i included my logo designs.
thank you

Target Market(s)

dentists

Industry/Entity Type

Communication

Requirements
Must have
• the included logo, whether the vertical or horizontal versions

```html
<!DOCTYPE html>
<html lang="en">
<head>
<meta charset="utf-8">
<title>Meridian Endodontics P.C. — Letterhead</title>
<link rel="stylesheet" href="https://fonts.googleapis.com/css2?family=Roboto+Slab:wght@600;700&display=swap">
<style>
  :root {
    --backdrop: #c9c9c9;
    --paper: #ffffff;
    --ink-blue: #1b9bd7;
    --ink-navy: #1d2a3a;
    --band-light: #dff3c8;
    --band-mid: #a9dc7a;
    --band-deep: #7dc242;
    --mark-blue: #2a8fd0;
    --watermark: rgba(120, 196, 236, 0.16);
  }
  * { margin: 0; padding: 0; box-sizing: border-box; }
  html, body {
    width: 1200px;
    height: 795px;
    overflow: hidden;
    background: var(--backdrop);
  }
  .canvas {
    position: relative;
    width: 1200px;
    height: 795px;
  }
  .letterhead {
    position: absolute;
    left: 308px;
    top: 20px;
    width: 584px;
    height: 755px;
    background: var(--paper);
    box-shadow: 0 2px 10px rgba(0, 0, 0, 0.18);
    font-family: "Roboto Slab", Georgia, serif;
    overflow: hidden;
  }
  .brand {
    position: absolute;
    display: flex;
    align-items: center;
    gap: 7px;
    color: var(--ink-navy);
    font-weight: 600;
    line-height: 1.05;
  }
  .brand-dot {
    width: 16px;
    height: 16px;
    border-radius: 50%;
    background: var(--mark-blue);
    flex: none;
  }
  .brand-name { font-size: 13px; letter-spacing: 0.5px; }
  .brand--header { left: 26px; top: 28px; }
  .brand--footer {
    left: 50%;
    bottom: 34px;
    transform: translateX(-50%);
  }
  .contact-band {
    position: absolute;
    right: 0;
    top: 62px;
    width: 56%;
    height: 120px;
    background: linear-gradient(180deg, var(--band-light) 0%, var(--band-mid) 55%, var(--band-deep) 100%);
  }
  .contact {
    position: absolute;
    right: 22px;
    top: 96px;
    text-align: right;
    color: var(--ink-blue);
    font-weight: 700;
    font-size: 13px;
    line-height: 17px;
  }
  .contact-name { margin-bottom: 2px; }
  .contact-web { margin-top: 14px; }
  .watermark {
    position: absolute;
    left: 50%;
    top: 410px;
    width: 260px;
    height: 260px;
    transform: translate(-50%, -50%);
    border-radius: 50%;
    background: var(--watermark);
  }
</style>
</head>
<body>
<main class="canvas">
  <article class="letterhead">
    <header>
      <div class="brand brand--header">
        <span class="brand-dot"></span>
        <span class="brand-name">Meridian Endodontics P.C.</span>
      </div>
      <div class="contact-band"></div>
      <address class="contact" style="font-style: normal;">
        <div class="contact-name">Gideon R. Whitfield DDS</div>
        <div>Phone: (716)482-9163</div>
        <div>Fax: (716)482-9170</div>
        <div>2847 Birchmont Avenue, Suite K</div>
        <div>West Harlow, NY 14391</div>
        <div class="contact-web">whitfieldroot.com</div>
      </address>
    </header>
    <div class="watermark" aria-hidden="true"></div>
    <footer>
      <div class="brand brand--footer">
        <span class="brand-dot"></span>
        <span class="brand-name">Meridian Endodontics P.C.</span>
      </div>
    </footer>
  </article>
</main>
</body>
</html>
```